VELTRIX Web Page

We need a corporate web site for a new company VELTRIX Corporation. VELTRIX is a technology company that has developed a new virtualization solution for corporate applications. Our target customers are IT professionals. We have a logo, which we will provide.

Final design should communicate: innovation, stability, professionalism

Industry/Entity Type

It Company

```html
<!DOCTYPE html>
<html lang="en">
<head>
<meta charset="utf-8">
<title>VELTRIX Corporation</title>
<link rel="stylesheet" href="https://fonts.googleapis.com/css2?family=Open+Sans:wght@400;600&family=Oswald:wght@400&display=swap">
<style>
  :root {
    --page-dark: #22211d;
    --page-mid: #34322d;
    --page-glow: #4a473f;
    --band-light: rgba(160, 156, 144, 0.30);
    --band-shade: rgba(18, 18, 16, 0.55);
    --headline: #dcd8cc;
    --label: #d6d2c6;
    --chevron: #e6e3da;
    --footer-title: #c4c0b4;
    --footer-body: #5e5c54;
  }
  * { margin: 0; padding: 0; box-sizing: border-box; }
  html, body { width: 1200px; height: 725px; overflow: hidden; background: var(--page-dark); }
  .page {
    position: relative;
    width: 1200px;
    height: 725px;
    overflow: hidden;
    font-family: "Open Sans", sans-serif;
  }
  .backdrop {
    position: absolute;
    inset: 0;
    background:
      radial-gradient(ellipse 260px 120px at 600px 70px, rgba(90, 86, 76, 0.35) 0%, rgba(0,0,0,0) 100%),
      radial-gradient(ellipse 200px 90px at 600px 650px, rgba(80, 76, 68, 0.30) 0%, rgba(0,0,0,0) 100%),
      radial-gradient(ellipse 40px 200px at 150px 360px, rgba(170, 164, 148, 0.28) 0%, rgba(0,0,0,0) 100%),
      radial-gradient(ellipse 40px 200px at 1030px 360px, rgba(170, 164, 148, 0.28) 0%, rgba(0,0,0,0) 100%),
      radial-gradient(ellipse 560px 330px at 595px 360px, var(--page-glow) 0%, var(--page-mid) 50%, var(--page-dark) 100%);
  }
  .hero-band {
    position: absolute;
    left: 178px;
    top: 176px;
    width: 829px;
    height: 367px;
    background:
      radial-gradient(ellipse 230px 170px at 470px 170px, var(--band-shade) 0%, rgba(0,0,0,0) 100%),
      radial-gradient(ellipse 180px 200px at 780px 180px, rgba(190, 186, 172, 0.12) 0%, rgba(0,0,0,0) 100%),
      var(--band-light);
  }
  .brand-label {
    position: absolute;
    left: 231px;
    top: 133px;
    font-size: 15px;
    color: var(--label);
    letter-spacing: 0.1px;
  }
  .headline-bullet {
    position: absolute;
    left: 221px;
    top: 214px;
    width: 23px;
    height: 23px;
    border-radius: 50%;
    background: var(--headline);
  }
  .headline {
    position: absolute;
    left: 268px;
    top: 200px;
    font-size: 68px;
    line-height: 59px;
    font-weight: 600;
    letter-spacing: -1px;
    color: var(--headline);
  }
  .chevrons {
    position: absolute;
    left: 0;
    top: 0;
  }
  .footer {
    position: absolute;
    left: 420px;
    top: 561px;
    width: 360px;
    text-align: center;
  }
  .footer-title {
    font-family: "Oswald", sans-serif;
    font-size: 8.5px;
    letter-spacing: 0.3px;
    color: var(--footer-title);
  }
  .footer-text {
    margin: 10px auto 0;
    width: 324px;
    font-size: 9.5px;
    line-height: 12.5px;
    color: var(--footer-body);
  }
  .footer-dot {
    display: inline-block;
    width: 9px;
    height: 9px;
    margin-right: 6px;
    vertical-align: -1px;
    border-radius: 50%;
    background: var(--footer-body);
  }
</style>
</head>
<body>
<main class="page">
  <div class="backdrop" role="img" aria-label="Dark close-up photograph of dandelion seed heads filling the page"></div>
  <div class="hero-band" role="img" aria-label="Lighter band of the dandelion photograph behind the headline"></div>

  <p class="brand-label">VELTRIX corp.</p>

  <span class="headline-bullet"></span>
  <h1 class="headline">A new<br>virtualization<br>solution for<br>corporate<br>applications</h1>

  <svg class="chevrons" width="1200" height="725" viewBox="0 0 1200 725" aria-hidden="true">
    <g fill="none" stroke="var(--chevron)" stroke-width="1.2">
      <polyline points="719,176 820,364 711,543"/>
      <polyline points="775,176 876,364 767,543"/>
      <polyline points="831,176 932,364 823,543"/>
    </g>
  </svg>

  <footer class="footer">
    <p class="footer-title">VELTRIX CORP. COPYRIGHT 2013</p>
    <p class="footer-text"><span class="footer-dot"></span>Lorem ipsum dolor sit amet, consectetur adipiscing elit. Aenean pulvinar augue et tortor posuere, et adipiscing odio eleifend. Sed felis ipsum, consequat id lectus sed, ornare suscipit dolor. Phasellus varius pellentesque libero, sed porttitor ipsum accumsan ut. Nullam sed vulputate eros, nec lacinia felis.</p>
  </footer>
</main>
</body>
</html>
```